My garage customisation company needs a business card

I need a business card design for my company "Shed Wizards"
I provide fully customised garage solutions for your previously cluttered, waste of space. My logo was just completed and can be provided if needed. I need the card to be clean, classy and eye catching.
Thank you

Target Market(s)

Men and Woman Home Owners

Industry/Entity Type

Business

Contact Information for Business Card

Jonathan Pell
jon@shedwizards.net
shedwizards.net

It's Time To Take Back Your Garage... From simple storage solutions to fully customised from the floor up, we've got you covered.

Requirements
Must have
• Logo
• Name
• Email Address
• Website
• Brief Description of what we do
Nice to have
• Back ground picture of Before and After

```html
<!DOCTYPE html>
<html lang="en">
<head>
<meta charset="utf-8">
<title>Shed Wizards – Business Card</title>
<link href="https://fonts.googleapis.com/css2?family=Roboto+Condensed:wght@400;700&family=Roboto:wght@300;400&display=swap" rel="stylesheet">
<style>
  :root {
    --page-bg: #d9dadc;
    --card-bg: #1c1c1d;
    --card-bg-light: #2a2a2b;
    --accent: #f26c2f;
    --text-light: #c9c9cb;
    --text-grey: #b3b3b6;
  }
  * { margin: 0; padding: 0; box-sizing: border-box; }
  html, body { width: 1200px; height: 1200px; overflow: hidden; }
  body {
    background: var(--page-bg);
    position: relative;
    font-family: "Roboto", sans-serif;
  }
  .card {
    position: absolute;
    left: 182px;
    width: 839px;
    height: 475px;
    background: radial-gradient(ellipse at 50% 35%, var(--card-bg-light) 0%, var(--card-bg) 70%);
    overflow: hidden;
  }
  .card--front { top: 79px; }
  .card--back { top: 624px; }

  .brand {
    position: absolute;
    display: flex;
    align-items: center;
    gap: 14px;
    font-family: "Roboto Condensed", sans-serif;
    font-weight: 700;
    color: var(--accent);
    text-transform: uppercase;
    white-space: nowrap;
  }
  .brand__mark { background: var(--accent); flex: none; }

  .card--front .brand {
    left: 0; right: 0; top: 130px;
    justify-content: center;
    font-size: 72px;
    letter-spacing: 2px;
  }
  .card--front .brand__mark { width: 44px; height: 44px; }

  .front__tagline {
    position: absolute;
    left: 0; right: 0; top: 330px;
    text-align: center;
    font-family: "Roboto Condensed", sans-serif;
    font-weight: 700;
    font-size: 33px;
    color: var(--accent);
  }
  .front__web {
    position: absolute;
    left: 0; right: 0; top: 386px;
    text-align: center;
    font-weight: 300;
    font-size: 26px;
    color: var(--text-light);
  }

  .card--back .brand {
    left: 30px; width: 334px; top: 108px;
    justify-content: center;
    font-size: 40px;
    gap: 10px;
  }
  .card--back .brand__mark { width: 26px; height: 26px; }

  .back__about {
    position: absolute;
    left: 20px; width: 354px; top: 240px;
    text-align: center;
    font-size: 21px;
    line-height: 25.5px;
    color: var(--accent);
  }

  .compare__label {
    position: absolute;
    top: 36px;
    font-family: "Roboto", sans-serif;
    font-size: 20px;
    color: var(--accent);
    transform: translateX(-50%);
  }
  .compare__label--before { left: 496px; }
  .compare__label--after { left: 720px; }
  .compare__photo {
    position: absolute;
    top: 65px; height: 130px;
    background: var(--accent);
  }
  .compare__photo--before { left: 373px; width: 227px; }
  .compare__photo--after { left: 616px; width: 223px; }

  .contact {
    position: absolute;
    right: 79px;
    text-align: right;
    white-space: nowrap;
  }
  .contact__name {
    top: 237px;
    font-family: "Roboto Condensed", sans-serif;
    font-weight: 700;
    font-size: 42px;
    color: var(--accent);
  }
  .contact__phone { top: 295px; font-family: "Roboto Condensed", sans-serif; font-size: 23px; color: var(--text-grey); }
  .contact__email { top: 335px; font-family: "Roboto Condensed", sans-serif; font-size: 23px; color: var(--text-grey); }
  .contact__web { top: 382px; right: 84px; font-weight: 300; font-size: 27px; color: var(--text-light); }
</style>
</head>
<body>
  <section class="card card--front">
    <div class="brand"><span class="brand__mark"></span>Shed Wizards</div>
    <p class="front__tagline">FULLY CUSTOMISED GARAGE SOLUTIONS</p>
    <p class="front__web">WWW.SHEDWIZARDS.NET</p>
  </section>

  <section class="card card--back">
    <div class="brand"><span class="brand__mark"></span>Shed Wizards</div>
    <p class="back__about">It's Time To Take Back<br>Your Garage...<br>From simple storage<br>solutions to fully customised<br>from the floor up,<br>we've got you covered.</p>

    <span class="compare__label compare__label--before">BEFORE</span>
    <span class="compare__label compare__label--after">AFTER</span>
    <div class="compare__photo compare__photo--before" role="img" aria-label="Photo of a cluttered garage before the makeover"></div>
    <div class="compare__photo compare__photo--after" role="img" aria-label="Photo of the organised garage after the makeover"></div>

    <p class="contact contact__name">JONATHAN PELL</p>
    <p class="contact contact__phone">555.014.0382</p>
    <p class="contact contact__email">jon@shedwizards.net</p>
    <p class="contact contact__web">WWW.SHEDWIZARDS.NET</p>
  </section>
</body>
</html>
```